Trying to create a web site off this static page

I am trying to create a seperate web site for this specific page. https://brolandathletics.com/hire-a-star/ I am still trying to figure out the domain name, for now, I will use Gold Roster as the name. I want to use the same pictures, but much more eye catching. Help me come up with something nice, something i can use to market to my thousands of customers. Maybe some flash. Something dramatic. I have some more content that I would like to add as well, but in the meantime, lets see what you come up with. Good luck and thanks
Updates

Some of these are really great. I may extend this for a few days... Please is the pictures from the Broland Athletics web site, but I want to make a few changes.... I want the name of the site changes to LuxeHours.com and as far as columns and tabs on the site, These are the tabs that I want. Please work with these and make the changes.

Our Talent

Past Client Experiences

ABout Us ( Our Philosophy)

Our Process

Ideas

Business Opportunities/ Warm Introductions

For the front page, I would like this content added in

FRONT PAGE Use this tag line somewhere "Where Dreams Become Luxe Experiences
Exclusive talent. Tailored events. Memories that last a lifetime."

Welcome to Luxe Hours

Where unforgettable moments are made.

At Luxe Hours, we connect individuals, businesses, and organizations with the world’s most recognizable athletes, entertainers, and celebrities. Whether it’s a private celebration, a corporate event, or a once-in-a-lifetime experience, our team specializes in making the impossible possible.

What We Do

Celebrity Bookings – From iconic musicians to legendary athletes, we secure top-tier talent for parties, concerts, and corporate functions.

Corporate Engagements – Motivate, inspire, and entertain your team with appearances from world-class speakers and sports legends.

Private Experiences – Fishing trips with Grand Gridiron Final champions, golf outings with All-Stars, tequila tastings with Hall of Famers—our clients have done it all.

University & Charity Events – Elevate your fundraiser, gala, or campus program with star power that draws attention and delivers impact.

VIP Appearances – From sitting courtside at the Showcase Classic with an PBL legend to sparring with Rick Dunmore, no dream is too big.

Why Choose Luxe Hours?

Exclusive Access – We work directly with celebrities and their management teams to deliver authentic, unforgettable experiences.

Proven Track Record – From Summit 400 companies to private clients, we’ve orchestrated events with some of the most famous names in the world.

Custom Experiences – Every event is unique. We tailor each booking to fit your vision, budget, and audience.

Confidential & Professional – Our clients trust us to deliver world-class experiences with complete discretion and flawless execution.

Let’s Make It Happen

Whether you’re planning a corporate retreat, a milestone celebration, or a private experience you’ll never forget, LuxeHours.com is your partner in making it extraordinary.

👉 If you can dream it, we can make it happen.

```html
<!DOCTYPE html>
<html lang="en">
<head>
<meta charset="utf-8">
<title>Luxe Hours</title>
<link rel="stylesheet" href="https://fonts.googleapis.com/css2?family=Manrope:wght@400;500;600;700&display=swap">
<style>
:root{
  --red:#e8321f;
  --ink:#151515;
  --text:#2a2a2a;
  --blush:#fdf0ee;
  --blush-soft:#fff7f6;
  --white:#ffffff;
  --black:#050505;
  --muted:#9a9a9a;
}
*{box-sizing:border-box;margin:0;padding:0}
html,body{width:1200px;height:5172px;overflow:hidden}
body{position:relative;font-family:"Manrope",Arial,sans-serif;color:var(--text);background:var(--white)}
.abs{position:absolute}
.btn{position:absolute;display:flex;align-items:center;justify-content:center;border:1.5px solid var(--red);border-radius:16px;color:var(--red);font-size:10px;font-weight:600;background:var(--white);height:30px}
.btn.solid{background:var(--red);color:var(--white)}
.photo{position:absolute}

/* header */
.site-header{position:absolute;left:0;top:0;width:1200px;height:62px;background:var(--white)}
.brand{position:absolute;font-weight:700;color:var(--ink)}
.brand .accent{color:var(--red)}
.nav{position:absolute;left:460px;top:24px;display:flex;gap:24px;font-size:10px;font-weight:600;color:var(--ink)}
.nav .active{color:var(--red)}
.login{position:absolute;left:876px;top:16px;width:84px;height:28px;border-radius:14px;background:var(--black);color:var(--white);font-size:10px;font-weight:600;display:flex;align-items:center;justify-content:center;gap:6px}

/* hero */
.hero{position:absolute;left:0;top:62px;width:1200px;height:470px;background:linear-gradient(160deg,#6b5a48 0%,#3b3733 45%,#22262b 100%)}
.hero h1{position:absolute;left:0;top:128px;width:1200px;text-align:center;color:var(--white);font-size:39px;font-weight:600;line-height:50px;text-shadow:0 2px 8px rgba(0,0,0,.4)}

/* about */
.about{position:absolute;left:0;top:532px;width:1200px;height:620px;background:linear-gradient(180deg,var(--white) 0%,var(--blush) 100%)}
.eyebrow{font-size:11px;font-weight:600;color:var(--red)}
.section-title{font-size:29px;font-weight:500;color:var(--ink)}
.red-head{color:var(--red);font-weight:600}
.small{font-size:11px;line-height:19px;color:var(--text)}

/* services */
.service h3{position:absolute;font-size:24px;font-weight:600;color:var(--red)}
.service p{position:absolute;width:350px;font-size:13.5px;line-height:25px;color:var(--text)}
.frame{position:absolute;border:1.5px solid var(--red)}

/* why */
.why{position:absolute;left:0;top:3300px;width:1200px;height:720px;background:var(--blush)}
.feat h4{position:absolute;font-size:12.5px;line-height:17px;font-weight:500;color:var(--ink)}
.feat h4 b{font-weight:700}
.feat p{position:absolute;width:190px;font-size:9.5px;line-height:14px;color:var(--text)}

/* testimonial */
.quote{font-size:13.5px;line-height:25px;color:var(--text)}

/* cta */
.cta{position:absolute;left:106px;top:4490px;width:988px;height:380px;background:var(--red);color:var(--white);text-align:center}
.cta h2{margin-top:64px;font-size:29px;font-weight:700}
.cta p{margin-top:30px;font-size:18px;line-height:30px}
.cta .tag{margin-top:20px;font-size:20px}

/* footer */
.footer{position:absolute;left:0;top:4712px;width:1200px;height:460px;background:var(--black);color:var(--white)}
.footer h5{position:absolute;font-size:12px;font-weight:700}
.footer .f-small{position:absolute;font-size:9.5px;line-height:18px}
.social{position:absolute;width:30px;height:30px;border-radius:50%;background:var(--white)}
</style>
</head>
<body>

<header class="site-header">
  <div class="brand" style="left:106px;top:18px;font-size:20px"><span class="accent">Luxe</span> Hours</div>
  <nav class="nav">
    <span class="active">Home</span><span>Our talent</span><span>About</span><span>Our process</span><span>Reviews</span><span>Contact us</span>
  </nav>
  <div class="login">
    <svg width="9" height="9" viewBox="0 0 10 10"><circle cx="5" cy="3" r="2.2" fill="#fff"/><path d="M1 10c0-3 2-4.5 4-4.5S9 7 9 10z" fill="#fff"/></svg>Login
  </div>
  <div class="btn" style="left:966px;top:16px;width:128px;height:28px">Book Your Events</div>
</header>

<section class="hero" role="img" aria-label="Guests mingling and raising glasses at an exclusive evening party">
  <h1>Where dreams become luxe experiences<br>Exclusive talent. Tailored events. Memories<br>that last a lifetime.</h1>
  <div class="btn solid" style="left:536px;top:310px;width:128px;background:var(--white);color:var(--red)">Book Your Events</div>
</section>

<section class="about">
  <svg class="abs" style="left:360px;top:100px" width="500" height="320" viewBox="0 0 500 320"><path d="M10 310 A240 240 0 0 1 490 310" fill="none" stroke="#f1d9d5" stroke-width="1"/></svg>
  <div class="abs eyebrow" style="left:200px;top:106px">About us</div>
  <h2 class="abs section-title" style="left:432px;top:94px">Welcome to Luxe Hours</h2>
  <div class="abs" style="left:432px;top:168px;width:568px;height:1px;background:#e9d3cf"></div>
  <div class="photo" style="left:200px;top:225px;width:205px;height:275px;background:linear-gradient(150deg,#6f5a4c,#b79b85 55%,#3f4450)" role="img" aria-label="Friends laughing together at a celebration"></div>
  <div class="photo" style="left:432px;top:200px;width:223px;height:325px;background:linear-gradient(160deg,#c9cfd4,#7d7a76 50%,#2f343a)" role="img" aria-label="Smiling man in a white shirt meeting guests"></div>
  <h3 class="abs red-head" style="left:693px;top:244px;width:320px;font-size:19px;line-height:26px">Where unforgettable moments are made.</h3>
  <p class="abs small" style="left:693px;top:308px;width:295px;font-size:10.5px">At Luxe Hours, we connect individuals, businesses, and organizations with the world's most recognizable athletes, entertainers, and celebrities. Whether it's a private celebration, a corporate event, or a once-in-a-lifetime experience, our team specializes in making the impossible possible.</p>
  <div class="btn" style="left:693px;top:450px;width:114px">Discover More</div>
</section>

<section class="services">
  <h2 class="abs section-title" style="left:0;top:1230px;width:1200px;text-align:center">What we do</h2>

  <div class="service">
    <div class="frame" style="left:650px;top:1305px;width:280px;height:310px"></div>
    <div class="photo" style="left:668px;top:1322px;width:332px;height:343px;background:linear-gradient(150deg,#8a2b25,#c79a6c 50%,#3a2c2a)" role="img" aria-label="Celebrity signing autographs on a red carpet"></div>
    <h3 style="left:200px;top:1395px">Celebrity bookings</h3>
    <p style="left:200px;top:1440px">From iconic musicians to legendary athletes, we secure top-tier talent for parties, concerts, and corporate functions.</p>
    <div class="btn" style="left:200px;top:1543px;width:126px">Book Your Events</div>
  </div>

  <div class="service">
    <div class="frame" style="left:268px;top:1695px;width:282px;height:305px"></div>
    <div class="photo" style="left:200px;top:1712px;width:332px;height:343px;background:linear-gradient(160deg,#2d3a4a,#8b9098 50%,#c9b8a4)" role="img" aria-label="Team members joining hands in an office"></div>
    <h3 style="left:612px;top:1785px">Corporate engagements</h3>
    <p style="left:612px;top:1830px">Motivate, inspire, and entertain your team with appearances from world-class speakers and ports legends.</p>
    <div class="btn" style="left:612px;top:1933px;width:126px">Book Your Events</div>
  </div>

  <div class="service">
    <div class="frame" style="left:650px;top:2085px;width:280px;height:310px"></div>
    <div class="photo" style="left:668px;top:2102px;width:332px;height:343px;background:linear-gradient(150deg,#5a1f2c,#c4506a 45%,#e6b08a)" role="img" aria-label="Group of friends toasting with champagne"></div>
    <h3 style="left:200px;top:2175px">Private experiences</h3>
    <p style="left:200px;top:2220px">Fishing trips with Grand Gridiron Final champions, golf outings with all-stars, tequila tastings with hall of famers—our clients have done it all.</p>
    <div class="btn" style="left:200px;top:2323px;width:126px">Book Your Events</div>
  </div>

  <div class="service">
    <div class="frame" style="left:268px;top:2475px;width:282px;height:305px"></div>
    <div class="photo" style="left:200px;top:2492px;width:332px;height:343px;background:linear-gradient(160deg,#6d8a5c,#3f8fc0 50%,#c9ad86)" role="img" aria-label="Volunteer in a blue shirt carrying a donation box"></div>
    <h3 style="left:612px;top:2565px">University &amp; charity events</h3>
    <p style="left:612px;top:2610px">Elevate your fundraiser, gala, or campus program with star power that draws attention and delivers impact.</p>
    <div class="btn" style="left:612px;top:2713px;width:126px">Book Your Events</div>
  </div>

  <div class="service">
    <div class="frame" style="left:650px;top:2865px;width:280px;height:310px"></div>
    <div class="photo" style="left:668px;top:2882px;width:332px;height:343px;background:linear-gradient(150deg,#2a2624,#7a6a62 50%,#e3c9c0)" role="img" aria-label="Star in an evening dress facing photographers at a premiere"></div>
    <h3 style="left:200px;top:2955px">VIP appearances</h3>
    <p style="left:200px;top:3000px">From sitting courtside at the Showcase Classic with an PBL legend to sparring with Rick Dunmore, no dream is too big.</p>
    <div class="btn" style="left:200px;top:3103px;width:126px">Book Your Events</div>
  </div>
</section>

<section class="why">
  <div class="photo" style="left:106px;top:78px;width:482px;height:567px;background:linear-gradient(140deg,#6a7f92,#c9a98c 45%,#3d6f78)" role="img" aria-label="Two professional women reviewing notes together"></div>
  <h2 class="abs section-title" style="left:650px;top:112px">Why choose Luxe Hours?</h2>
  <div class="abs" style="left:865px;top:170px;width:1px;height:380px;background:#e7c9c4"></div>
  <div class="abs" style="left:650px;top:358px;width:445px;height:1px;background:#e7c9c4"></div>

  <div class="feat">
    <svg class="abs" style="left:650px;top:176px" width="44" height="34" viewBox="0 0 44 34"><path d="M4 26 L2 6 L13 16 L22 3 L31 16 L42 6 L40 26 Z" fill="none" stroke="#e8321f" stroke-width="2"/><rect x="4" y="28" width="36" height="4" fill="none" stroke="#111" stroke-width="1.5"/></svg>
    <h4 style="left:650px;top:226px">Exclusive<br><b>access</b></h4>
    <p style="left:650px;top:270px">We work directly with celebrities and their management teams to deliver authentic, unforgettable experiences.</p>

    <svg class="abs" style="left:880px;top:172px" width="40" height="38" viewBox="0 0 40 38"><circle cx="9" cy="9" r="7" fill="none" stroke="#e8321f" stroke-width="2"/><rect x="18" y="22" width="5" height="14" fill="#e8321f"/><rect x="25" y="16" width="5" height="20" fill="#e8321f"/><rect x="32" y="10" width="5" height="26" fill="#111"/><line x1="2" y1="36" x2="40" y2="36" stroke="#111" stroke-width="1.5"/></svg>
    <h4 style="left:880px;top:226px">Proven<br><b>track record</b></h4>
    <p style="left:880px;top:270px">From Summit 400 companies to private clients, we've orchestrated events with some of the most famous names in the world.</p>

    <svg class="abs" style="left:650px;top:370px" width="40" height="40" viewBox="0 0 40 40"><path d="M20 38 C10 26 6 20 6 14 A14 14 0 0 1 34 14 C34 20 30 26 20 38 Z" fill="none" stroke="#e8321f" stroke-width="2"/><circle cx="20" cy="14" r="5" fill="none" stroke="#111" stroke-width="1.5"/></svg>
    <h4 style="left:650px;top:430px">Custom<br><b>experiences</b></h4>
    <p style="left:650px;top:474px">Every event is unique. We tailor each booking to fit your vision, budget, and audience.</p>

    <svg class="abs" style="left:880px;top:370px" width="40" height="40" viewBox="0 0 40 40"><rect x="4" y="18" width="8" height="18" fill="none" stroke="#111" stroke-width="1.5"/><path d="M12 20 L20 6 C24 6 24 10 23 16 L34 16 C36 16 37 18 36 20 L33 34 C32 36 31 36 29 36 L12 36" fill="none" stroke="#e8321f" stroke-width="2"/></svg>
    <h4 style="left:880px;top:430px">Confidential &amp;<br><b>professional</b></h4>
    <p style="left:880px;top:474px">Our clients trust us to deliver world-class experiences with complete discretion and flawless execution.</p>
  </div>

  <div class="btn solid" style="left:650px;top:580px;width:126px">Book Your Events</div>
</section>

<section class="reviews">
  <h2 class="abs section-title" style="left:200px;top:4100px">Happy clients say</h2>
  <svg class="abs" style="left:930px;top:4115px" width="72" height="32" viewBox="0 0 72 32"><circle cx="16" cy="16" r="14" fill="none" stroke="#e8321f" stroke-width="1.2"/><path d="M19 11 L13 16 L19 21" fill="none" stroke="#e8321f" stroke-width="1.5"/><circle cx="54" cy="16" r="14" fill="none" stroke="#e8321f" stroke-width="1.2"/><path d="M51 11 L57 16 L51 21" fill="none" stroke="#e8321f" stroke-width="1.5"/></svg>
  <svg class="abs" style="left:196px;top:4233px" width="170" height="170" viewBox="0 0 170 170"><rect x="35" y="35" width="100" height="100" transform="rotate(45 85 85)" fill="none" stroke="#e8321f" stroke-width="1.5"/></svg>
  <div class="photo" style="left:231px;top:4268px;width:100px;height:100px;transform:rotate(45deg);background:linear-gradient(135deg,#d9c4a8,#c8283a 60%,#6b1f26)" role="img" aria-label="Portrait of a happy client"></div>
  <div class="abs" style="left:395px;top:4195px;width:1.5px;height:200px;background:var(--red)"></div>
  <div class="abs quote" style="left:445px;top:4200px;font-weight:500;color:var(--ink)">“It is a long established fact that a reader.”</div>
  <p class="abs quote" style="left:445px;top:4240px;width:490px">There are many variations of passages of Lorem Ipsum available, but the majority have suffered alteration in some form, by injected humour, or randomised words which don't look even slightly</p>
  <div class="abs" style="left:445px;top:4330px;font-size:17px;font-weight:500;color:var(--ink)">Standard Chunk</div>
  <div class="btn" style="left:445px;top:4433px;width:124px">View All Reviews</div>
</section>

<footer class="footer">
  <div class="brand" style="left:106px;top:225px;font-size:27px;color:var(--white)"><span class="accent">Luxe</span> Hours</div>
  <div class="social" style="left:128px;top:281px" role="img" aria-label="Social profile link"></div>
  <div class="social" style="left:166px;top:281px" role="img" aria-label="Social profile link"></div>
  <div class="social" style="left:204px;top:281px" role="img" aria-label="Social profile link"></div>
  <div class="social" style="left:242px;top:281px" role="img" aria-label="Social profile link"></div>

  <h5 style="left:350px;top:222px">Contact us</h5>
  <svg class="abs" style="left:350px;top:258px" width="10" height="80" viewBox="0 0 10 80"><path d="M2 1 L4 1 L5 4 L4 5 C5 7 6 8 7 8 L8 7 L10 8 L10 10 C6 10 1 6 2 1 Z" fill="#e8321f"/><rect x="0.5" y="28" width="9" height="7" fill="none" stroke="#e8321f"/><path d="M0.5 28 L5 32 L9.5 28" fill="none" stroke="#e8321f"/><path d="M5 64 C2 60 1 58 1 56 A4 4 0 0 1 9 56 C9 58 8 60 5 64 Z" fill="#e8321f"/></svg>
  <div class="f-small" style="left:372px;top:255px">+12 555 - 014 - 392</div>
  <div class="f-small" style="left:372px;top:282px">hello@luxehours.com</div>
  <div class="f-small" style="left:372px;top:308px;width:190px">88 Harbor Lane, Suite 210, Brookvale<br>NC 27999</div>

  <h5 style="left:605px;top:222px">Quick links</h5>
  <div class="f-small" style="left:605px;top:255px">Home<br>Our talent<br>About<br>Our process</div>
  <div class="f-small" style="left:686px;top:255px">Reviews<br>Contact us</div>

  <h5 style="left:793px;top:222px">Subscribe newsletter</h5>
  <div class="abs" style="left:793px;top:271px;width:301px;height:30px;border-radius:15px;background:var(--white);color:#555;font-size:9px;padding:9px 16px">Enter your email...</div>
  <div class="abs" style="left:793px;top:313px;width:92px;height:28px;border-radius:14px;background:var(--red);font-size:10px;font-weight:600;display:flex;align-items:center;justify-content:center">Subscribe</div>

  <div class="abs" style="left:106px;top:388px;width:988px;height:1px;background:#2a2a2a"></div>
  <div class="f-small" style="left:106px;top:418px">© 2025 <span style="color:var(--red)">Luxe Hours</span>. All rights Reserved.</div>
  <div class="f-small" style="left:382px;top:418px;word-spacing:2px">Cookie Policy &nbsp;&nbsp; | &nbsp;&nbsp; Privacy Statement &nbsp;&nbsp; | &nbsp;&nbsp; Disclaimer</div>
  <svg class="abs" style="left:1135px;top:400px" width="20" height="22" viewBox="0 0 20 22"><path d="M10 1 L19 21 L10 15 L1 21 Z" fill="#e8321f"/></svg>
</footer>

<section class="cta">
  <h2>Let's Make it Happen</h2>
  <p>Whether you're planning a corporate retreat, a milestone celebration,<br>or a private experience you'll never forget, LuxeHours.com is your partner in<br>making it extraordinary.</p>
  <p class="tag">If You Can Dream It, We Can Make It Happen.</p>
  <div class="btn" style="left:430px;top:304px;width:128px;background:transparent;border-color:var(--white);color:var(--white)">Book Your Events</div>
</section>

</body>
</html>
```